Information Package (Hail Insurance Claim)

TheRenewalWorkshop.com is a new company to the Calgary Alberta area. We want a flyer for potential clients to give them tips on how to deal with the insurance process, how we can represent them, and what to do for next steps.
Also in the flyer we want to introduce clients to the products we use along with the experience we have.

Target Market(s)

Homeowners who have just got hit with hail

Font styles to use
Serif

Requirements
Must have
• Must have two sides.
phone number is 403-617-8094
email is Claims@TheRenewalWorkshop.example
Trusted Brands: Brevanta, Ferrick Valemont, PLU, DRW
Ferrick valemont website has their roofing products and system we use.
I have attached our logo design and want to keep that theme.
Also this link https://prairietopsolutions.example/roof-insurance-claims/ has some great information on steps.
Products to include from these links: https://www.ferrickvalemont.example/roofing/shingles
https://www.summitpeakshingle.example/roof-shingles-types/

```html
<!DOCTYPE html>
<html lang="en">
<head>
<meta charset="utf-8">
<title>Insurance Claims &amp; Hail Damage – TheRenewalWorkshop.com</title>
<link href="https://fonts.googleapis.com/css2?family=Bebas+Neue&family=Lato:wght@400;700&display=swap" rel="stylesheet">
<style>
:root{
  --bg:#7a7a7a;
  --navy:#2b3a55;
  --teal:#5bbcb2;
  --yellow:#f2c94c;
  --ink:#2a2a2a;
  --white:#ffffff;
  --frame:#5d6f8f;
}
*{box-sizing:border-box;margin:0;padding:0}
html,body{width:1200px;height:1200px;overflow:hidden}
body{background:var(--bg);font-family:'Lato',sans-serif;color:var(--ink);position:relative}
.page{position:absolute;top:247px;width:506px;height:709px;background:var(--white);overflow:hidden}
.page--front{left:96px}
.page--back{left:614px}
.abs{position:absolute}

/* header */
.front-header{left:0;top:0;width:506px;height:102px}
.front-title{left:14px;top:20px;font-family:'Bebas Neue',sans-serif;line-height:1;white-space:nowrap}
.front-title .line-1{color:var(--teal);font-size:26px}
.front-title .line-2{color:var(--yellow);font-size:34px;margin-top:2px}
.brand{display:flex;align-items:center;gap:5px;font-family:'Lato',sans-serif;font-weight:700;font-size:9.5px;color:var(--navy);white-space:nowrap}
.brand-dot{width:13px;height:13px;border-radius:50%;background:var(--yellow);flex:none}
.front-brand{left:358px;top:45px}
.back-brand{left:22px;top:45px}

.intro{left:17px;top:112px;width:472px;font-size:6.6px;line-height:1.35}
.intro p+p{margin-top:5px}
.goal{left:16px;top:158px}
.goal-lead{color:var(--teal);font-size:17px;line-height:1}
.goal-sub{font-family:'Bebas Neue',sans-serif;color:var(--navy);font-size:14.5px;margin-top:4px;padding-bottom:2px;border-bottom:1.5px solid var(--yellow);width:400px}

.column{top:210px;display:flex;flex-direction:column}
.column--left{left:16px;width:222px}
.column--right{left:249px;width:240px}
.tip{display:flex;gap:5px;margin-bottom:10px}
.tip-num{flex:none;width:10px;height:10px;border-radius:50%;background:var(--teal);color:var(--white);font-size:6px;font-weight:700;display:flex;align-items:center;justify-content:center;margin-top:1px}
.tip h3{font-size:8.4px;font-weight:700;line-height:1.3;color:var(--navy);margin-bottom:4px}
.tip p{font-size:6.4px;line-height:1.35;text-align:justify}
.tip p+p{margin-top:5px}

/* footer */
.footer{left:0;top:673px;width:506px;height:36px}
.contact{top:673px;height:36px;display:flex;align-items:center;gap:5px;font-size:8.5px;color:var(--white);white-space:nowrap}
.contact svg{flex:none}
.contact--phone{left:32px}
.contact--mail{left:128px}
.contact--web{left:336px}

/* back */
.hero-photo{left:162px;top:0;width:344px;height:102px}
.back-lines{left:0;top:103px;width:506px;height:4px}
.photo{left:16px;width:247px;box-shadow:0 3px 4px rgba(0,0,0,.15)}
.photo--1{top:123px;height:184px;background:linear-gradient(160deg,#8aa0b8 0%,#a4683c 28%,#1d2433 45%,#222a3a 100%)}
.photo--2{top:328px;height:166px;background:linear-gradient(150deg,#8a7768 0%,#a0887a 50%,#6b8a4a 100%)}
.photo--3{top:515px;height:140px;background:linear-gradient(135deg,#3f4a46 0%,#586a62 45%,#a05a32 52%,#5f6f63 60%,#6f7e6a 100%)}
.swatch-box{left:280px;width:210px;border:1px solid var(--frame);padding:5px;display:grid;gap:5px 6px;background:var(--white)}
.swatch-box--1{top:123px;height:184px;grid-template-columns:repeat(3,1fr)}
.swatch-box--2{top:328px;height:166px;grid-template-columns:repeat(2,1fr)}
.swatch-box--3{top:515px;height:140px;grid-template-columns:repeat(3,1fr)}
.swatch{display:flex;flex-direction:column;font-size:3.6px;color:#555}
.swatch i{display:block;flex:1;margin-bottom:1px}
.swatch-box--2 .swatch{position:relative}
.swatch-box--2 .swatch i{margin:0}
.swatch-box--2 .swatch span{position:absolute;left:4px;bottom:5px;font-size:4.5px;font-weight:700;color:var(--white)}
</style>
</head>
<body>

<!-- Side one -->
<section class="page page--front">
  <svg class="abs front-header" viewBox="0 0 506 102" aria-hidden="true">
    <path d="M0 0H360L316 102H0Z" fill="var(--navy)"/>
    <path d="M0 102H316L318 104H0Z" fill="var(--yellow)"/>
    <rect x="316" y="101" width="190" height="2.5" fill="var(--teal)"/>
  </svg>
  <div class="abs front-title">
    <div class="line-1">Insurance Claims &amp; Hail Damage:</div>
    <div class="line-2">The Top 10 Misconceptions</div>
  </div>
  <div class="abs brand front-brand"><span class="brand-dot"></span>TheRenewalWorkshop.com</div>

  <div class="abs intro">
    <p>If you want to make sure your roof is done as soon as possible, call us today for a free roof quote. We'll help you with the roof insurance claims process and install your new roof in a timely manner.</p>
    <p>The hailstorm in August 2012 caused about $200 million of damages and you may have been affected, possibly without even realizing it. And you might be making some assumptions about the process that could have serious consequences.</p>
  </div>

  <div class="abs goal">
    <div class="goal-lead">Our goal is to provide you with a</div>
    <div class="goal-sub">Better understanding of the issues so you can get the result you deserve:</div>
  </div>

  <div class="abs column column--left">
    <div class="tip"><span class="tip-num">1</span><div>
      <h3>You're waiting to file your claim</h3>
      <p>You should contact the claims department of your insurance company as soon as possible and find out how long you have to file a claim. If you don't file a claim within the allowable time, usually one year, you may end up footing the bill yourself.</p>
      <p>And waiting for spring to file your claim could be a costly mistake.</p>
    </div></div>
    <div class="tip"><span class="tip-num">2</span><div>
      <h3>You think you have to use your insurer's preferred contractors</h3>
      <p>In most cases, insurers will not force you to use the contractors they recommend. Although their preferred contractors are reputable companies, there's no guarantee you will get the quality you deserve. Click here to learn more about preferred contractors.</p>
      <p>If you, or your friends and neighbours, have had a great experience with a different contractor, you will probably feel better about using them than trying someone new.</p>
      <p>We have successfully helped many homeowners with their insurance claims. We will do a free, detailed inspection of your roof and provide a complete report to your insurer.</p>
    </div></div>
    <div class="tip"><span class="tip-num">3</span><div>
      <h3>You're not sure if you have hail damage</h3>
      <p>Hail damage isn't always easy to spot. You may not see any damage and believe you just got lucky. But even the smallest amount of damage can cause leaks later.</p>
    </div></div>
    <div class="tip"><span class="tip-num">4</span><div>
      <h3>You don't think you have enough damage to file a claim</h3>
      <p>Even minor damage can cause serious, expensive leaks in the future. An inspection will confirm how much damage you have and whether your roof needs to be repaired or replaced.</p>
      <p>You should file a claim not matter how little damage you think you have. If it requires only minor repairs (less than your deductible), you don't have to proceed with your claim.</p>
    </div></div>
    <div class="tip"><span class="tip-num">5</span><div>
      <h3>You have a new home and believe the Provincial New Home Warranty Program will cover the hail damage</h3>
      <p>The warranty program only covers structural defects and defects in materials and workmanship. Hail damage is not covered.</p>
    </div></div>
  </div>

  <div class="abs column column--right">
    <div class="tip"><span class="tip-num">6</span><div>
      <h3>You believe the shingle manufacturer or roofing contractor warranties will cover the hail damage</h3>
      <p>Manufacturers' warranties specifically exclude hail damage. Similarly, roofing contractors offer warranties covering their workmanship, not acts of god. If you have hail damage, you should file a claim with your insurer as soon as possible.</p>
    </div></div>
    <div class="tip"><span class="tip-num">7</span><div>
      <h3>You don't want to file a claim because you don't want your policy cancelled or your rates to increase</h3>
      <p>Insurers aren't allowed to cancel your home policy due to these types of claims. Your insurance will remain in effect without any penalties to you.</p>
      <p>Insurance companies may be forced to raise rates for all homeowners after costly disasters such as hail or wind storms. Your personal rates, however, won't increase by filing a hail damage claim.</p>
      <p>If you don't file a claim and overall rates increase, you'll simply be subsidizing other homeowners who did file a claim.</p>
    </div></div>
    <div class="tip" style="margin-top:8px"><span class="tip-num">8</span><div>
      <h3>You filed a claim but want to wait until the spring or summer to get quotes to have the work done</h3>
      <p>Most people don't think of getting their roofs done in the winter. But the hailstorm will create spring chaos in the roofing industry.</p>
    </div></div>
    <div class="tip" style="margin-top:8px"><span class="tip-num">9</span><div>
      <h3>You received a payout from your insurance company and you'll find your own contractor, but there's no rush</h3>
      <p>You will likely have a hard time finding a quality contractor in the spring. See the above comments about spring roofing.</p>
    </div></div>
    <div class="tip" style="margin-top:8px"><span class="tip-num">10</span><div>
      <h3>You filed a claim but it was denied</h3>
      <p>After a major hailstorm, insurance adjusters and roofing contractors are swamped. As a result, you may not have had a thorough inspection of your roof or your claim may simply not have received the attention normally required.</p>
      <p>You have every right to appeal this decision, especially if you know your area was hit by hail and your neighbours have had their claims approved. You should get another independent, detailed inspection so you can provide your insurer with evidence that might have been overlooked.</p>
    </div></div>
  </div>

  <svg class="abs footer" viewBox="0 0 506 36" aria-hidden="true">
    <rect width="506" height="36" fill="var(--navy)"/>
    <path d="M310 0H506V36H326Z" fill="var(--teal)"/>
  </svg>
  <div class="abs contact contact--phone">
    <svg width="8" height="11" viewBox="0 0 8 11"><path d="M2 0.5 4 3 3 4.5Q3.5 6.5 5 7.5L6.5 7 8 9.5 6 10.8Q1 8 1 1Z" fill="var(--yellow)"/></svg>403-617-8094</div>
  <div class="abs contact contact--mail">
    <svg width="12" height="8" viewBox="0 0 12 8"><rect width="12" height="8" fill="var(--yellow)"/><path d="M0 0 6 5 12 0" fill="none" stroke="var(--navy)" stroke-width="1"/></svg>Claims@TheRenewalWorkshop.example</div>
  <div class="abs contact contact--web">
    <svg width="10" height="10" viewBox="0 0 10 10" fill="none" stroke="var(--navy)" stroke-width=".9"><circle cx="5" cy="5" r="4.4"/><ellipse cx="5" cy="5" rx="2" ry="4.4"/><path d="M.6 5H9.4"/></svg>TheRenewalWorkshop.com</div>
</section>

<!-- Side two -->
<section class="page page--back">
  <div class="abs brand back-brand"><span class="brand-dot"></span>TheRenewalWorkshop.com</div>
  <svg class="abs hero-photo" viewBox="0 0 344 102" role="img" aria-label="Photo of a shingled roof under a bright sky with trees">
    <defs><linearGradient id="sky" x1="0" y1="0" x2="0" y2="1">
      <stop offset="0" stop-color="#b8c7d6"/><stop offset=".55" stop-color="#8e9ca6"/><stop offset="1" stop-color="#4e5660"/></linearGradient></defs>
    <path d="M25 0H344V102H0Z" fill="url(#sky)"/>
  </svg>
  <svg class="abs back-lines" viewBox="0 0 506 4" aria-hidden="true">
    <rect width="316" height="2.5" fill="var(--yellow)"/>
    <rect x="318" width="188" height="2.5" fill="var(--teal)"/>
  </svg>

  <div class="abs photo photo--1" role="img" aria-label="Roofers laying underlayment and new shingle bundles on a residential roof"></div>
  <div class="abs photo photo--2" role="img" aria-label="Finished brown shingle roof with vents"></div>
  <div class="abs photo photo--3" role="img" aria-label="Green shingle roof around a brick chimney"></div>

  <div class="abs swatch-box swatch-box--1">
    <div class="swatch"><i style="background:#2d2c2b"></i>Dual Black</div>
    <div class="swatch"><i style="background:#55524d"></i>Charcoal Grey</div>
    <div class="swatch"><i style="background:#3b4047"></i>Harbour Blue</div>
    <div class="swatch"><i style="background:#7c7a76"></i>Dual Grey</div>
    <div class="swatch"><i style="background:#5a3f32"></i>Dual Brown</div>
    <div class="swatch"><i style="background:#4b4846"></i>Patriot Slate</div>
    <div class="swatch"><i style="background:#6b6458"></i>Driftwood</div>
    <div class="swatch"><i style="background:#6a4437"></i>Aged Redwood</div>
    <div class="swatch"><i style="background:#a9a7a4"></i>Super White</div>
    <div class="swatch"><i style="background:#6b2a22"></i>Riviera Red</div>
    <div class="swatch"><i style="background:#3f4d3b"></i>Vintage Green</div>
    <div class="swatch"><i style="background:#8a7665"></i>Beachwood</div>
  </div>
  <div class="abs swatch-box swatch-box--2">
    <div class="swatch"><i style="background:#4f4d4a"></i><span>Appalachian</span></div>
    <div class="swatch"><i style="background:#5e4236"></i><span>Sedona</span></div>
    <div class="swatch"><i style="background:#6d6f70"></i><span>Biscayne</span></div>
    <div class="swatch"><i style="background:#4a4235"></i><span>Cornerstone</span></div>
    <div class="swatch"><i style="background:#3e4145"></i><span>Glacier</span></div>
    <div class="swatch"><i style="background:#393a3b"></i><span>Castle Grey</span></div>
  </div>
  <div class="abs swatch-box swatch-box--3">
    <div class="swatch"><i style="background:#2f2e2d"></i>Dual Black</div>
    <div class="swatch"><i style="background:#67605a"></i>Charcoal Grey</div>
    <div class="swatch"><i style="background:#4a4c50"></i>Harvard Slate</div>
    <div class="swatch"><i style="background:#6a4a33"></i>Dual Brown</div>
    <div class="swatch"><i style="background:#594a40"></i>Heatherwood</div>
    <div class="swatch"><i style="background:#7a6a4a"></i>Weatherwood</div>
    <div class="swatch"><i style="background:#75463a"></i>Aged Redwood</div>
    <div class="swatch"><i style="background:#b07a4a"></i>Earthtone Cedar</div>
    <div class="swatch"><i style="background:#8a3328"></i>Riviera Red</div>
  </div>

  <svg class="abs footer" viewBox="0 0 506 36" aria-hidden="true">
    <rect width="506" height="36" fill="var(--navy)"/>
    <path d="M310 0H506V36H326Z" fill="var(--teal)"/>
  </svg>
  <div class="abs contact contact--phone">
    <svg width="8" height="11" viewBox="0 0 8 11"><path d="M2 0.5 4 3 3 4.5Q3.5 6.5 5 7.5L6.5 7 8 9.5 6 10.8Q1 8 1 1Z" fill="var(--yellow)"/></svg>403-617-8094</div>
  <div class="abs contact contact--mail">
    <svg width="12" height="8" viewBox="0 0 12 8"><rect width="12" height="8" fill="var(--yellow)"/><path d="M0 0 6 5 12 0" fill="none" stroke="var(--navy)" stroke-width="1"/></svg>Claims@TheRenewalWorkshop.example</div>
  <div class="abs contact contact--web">
    <svg width="10" height="10" viewBox="0 0 10 10" fill="none" stroke="var(--navy)" stroke-width=".9"><circle cx="5" cy="5" r="4.4"/><ellipse cx="5" cy="5" rx="2" ry="4.4"/><path d="M.6 5H9.4"/></svg>TheRenewalWorkshop.com</div>
</section>

</body>
</html>
```